Kelvoran Financial Web Design Contest

We would like for you to design a website for www.kelvoranfinancial.example. Kelvoran Financial is a CPA Firm offering accounting, auditing, and tax preparation services.

We would like to have a consistent feel with the logo, business card, envelope, and stationary designs that were created by another designer on ArtHive. Examples of each are attached. We would like the website to have a clean/modern style.

The website should include the following:

1. A general "Welcome" landing page
2. A "About the Company" page
3. A "Services Offered" page
4. A "Contact Us" form
5. A button for "Sign up for Newsletter"

Target Market(s)

Individuals and businesses that require accounting, auditing, and tax preparation services from a CPA.

Industry/Entity Type

Accounting

Coding

Number of Pages Required

Font styles to use
Other font styles liked:
• Trebuchet or similar

Requirements
Must have
• Consistent feel with logo and letterhead. The gray and blue bar on the letterhead should be incorporated into the website design.

```html
<!DOCTYPE html>
<html lang="en">
<head>
<meta charset="utf-8">
<title>Kelvoran Financial, LLC</title>
<link rel="stylesheet" href="https://fonts.googleapis.com/css2?family=Ubuntu:wght@400;500&family=Open+Sans:ital,wght@0,400;0,600;1,400&display=swap">
<style>
:root{
  --navy:#0b2a78;
  --navy-dark:#0a1d52;
  --ink:#333;
  --muted:#777;
  --rule:#e3e3e3;
  --paper:#f1f1f1;
  --grey-bar:#4a4a4a;
  --white:#fff;
}
*{box-sizing:border-box;margin:0;padding:0}
html,body{width:691px;height:1200px;overflow:hidden}
body{position:relative;background:var(--white);font-family:"Open Sans",Arial,sans-serif;color:var(--ink)}
.abs{position:absolute}
.heading{font-family:"Ubuntu","Trebuchet MS",sans-serif}

/* hero */
.hero{left:0;top:0;width:691px;height:403px;background:linear-gradient(120deg,#9aa0a8 0%,#5c6068 35%,#2c3038 70%,#1b2230 100%)}
.hero-shade{left:0;top:0;width:691px;height:403px;background:linear-gradient(180deg,rgba(255,255,255,.35) 0%,rgba(0,0,0,.1) 40%,rgba(0,0,0,.25) 100%)}
.brand{left:60px;top:28px;display:flex;align-items:center;gap:8px}
.brand-mark{width:18px;height:18px;border:2px solid var(--navy)}
.brand-name{font-family:"Ubuntu","Trebuchet MS",sans-serif;font-size:11px;font-weight:500;color:var(--navy);letter-spacing:.5px}
.nav{top:33px;left:350px;display:flex;gap:0}
.nav a{font-family:"Ubuntu","Trebuchet MS",sans-serif;font-size:8px;color:var(--white);text-decoration:none;position:absolute;white-space:nowrap}
.nav .active::after{content:"";position:absolute;left:0;right:0;top:14px;height:2px;background:var(--white)}
.hero-mark{left:315px;top:152px;width:68px;height:68px;border:4px solid var(--white)}
.hero-title{left:0;width:691px;top:225px;text-align:center;font-size:19px;color:var(--white);letter-spacing:1px}
.hero-rule{left:208px;top:251px;width:276px;height:1px;background:rgba(255,255,255,.6)}
.hero-tag{left:0;width:691px;top:254px;text-align:center;font-size:11.5px;color:var(--white);letter-spacing:1.6px}
.slide-arrow{top:205px;width:18px;height:18px;border:1px solid rgba(255,255,255,.5);border-radius:50%}

/* services */
.services{left:56px;top:344px;width:578px;height:170px;background:#f9f9f9;box-shadow:0 2px 8px rgba(0,0,0,.18);border-radius:2px}
.service{top:0;width:192px;height:170px;text-align:center}
.service + .service{border-left:1px solid #eee}
.service-icon{position:absolute;left:70px;top:17px;width:53px;height:53px;border-radius:50%;background:var(--navy-dark)}
.service-icon svg{position:absolute;left:14px;top:14px}
.service h3{position:absolute;top:81px;left:0;width:100%;font-family:"Ubuntu","Trebuchet MS",sans-serif;font-weight:400;font-size:8.5px;color:#333}
.service p{position:absolute;top:96px;left:16px;width:160px;font-size:6.3px;line-height:11.5px;color:#555}
.btn-slant{position:absolute;top:140px;left:52px;width:90px;height:16px}
.btn-slant span{position:absolute;left:32px;top:3px;font-size:6px;font-weight:600;color:var(--white)}
.services-tail{left:56px;top:514px;width:578px;height:18px}

/* welcome */
.welcome{left:0;top:555px;width:691px;height:296px;background:linear-gradient(180deg,#0c1f5c 0%,#142c72 50%,#0d1c4a 100%)}
.welcome h2{position:absolute;top:26px;left:0;width:691px;text-align:center;font-weight:400;font-size:22px;color:var(--white)}
.welcome-rule{position:absolute;left:212px;top:60px;width:266px;height:1px;background:rgba(255,255,255,.7)}
.welcome-dot{position:absolute;left:343px;top:58px;width:5px;height:5px;border-radius:50%;background:var(--white)}
.welcome p{position:absolute;top:72px;left:82px;width:527px;text-align:center;font-size:6.3px;line-height:12px;color:var(--white)}
.welcome .ghost{position:absolute;left:285px;top:120px;width:120px;height:22px}
.welcome .ghost span{position:absolute;left:40px;top:6px;font-size:6.5px;font-weight:600;color:var(--white)}
.person{top:162px;width:272px;height:103px;background:var(--white)}
.person-photo{position:absolute;left:0;top:0;width:112px;height:103px;background:linear-gradient(135deg,#b8cbe0,#7d95b5 60%,#d9dee6)}
.person h4{position:absolute;left:126px;top:13px;font-family:"Ubuntu","Trebuchet MS",sans-serif;font-weight:400;font-size:9px;color:var(--navy)}
.person p{position:absolute;left:126px;top:30px;width:136px;font-style:italic;font-size:6.2px;line-height:11.5px;color:#666}
.person .outline{position:absolute;left:124px;top:73px;padding:3px 7px;border:1px solid var(--navy);font-size:6.5px;color:var(--navy)}

/* newsletter */
.newsletter{left:0;top:851px;width:691px;height:170px;background:var(--paper)}
.newsletter h2{position:absolute;top:34px;width:691px;text-align:center;font-weight:400;font-size:15px;color:#444}
.newsletter p{position:absolute;top:60px;left:95px;width:501px;text-align:center;font-size:6.2px;line-height:13px;color:var(--muted)}
.field{position:absolute;top:99px;height:24px;background:var(--white);border:1px solid #ddd;font-size:6.2px;color:#aaa;padding:8px 9px}
.subscribe{position:absolute;left:472px;top:99px;width:100px;height:24px;background:var(--navy-dark);color:var(--white);font-size:7px;text-align:center;line-height:24px}

/* footer */
.band{left:0;top:1006px;width:691px;height:36px}
.footer-mark{left:57px;top:1070px;width:66px;height:66px;border:3px solid #e2e2e2}
.badge{top:1071px;height:30px;border:1px solid #ddd}
.social{top:1115px;width:16px;height:16px;border-radius:50%;background:#777}
.links{left:398px;top:1069px}
.links a{display:block;font-size:6.8px;color:#333;text-decoration:none;line-height:17px}
.contact{left:490px;top:1069px;font-size:6.8px;color:#444;line-height:11px}
.contact div{position:absolute;left:14px;width:160px}
.contact svg{position:absolute;left:0}
.legal-rule{left:57px;top:1168px;width:634px;height:1px;background:var(--rule)}
.legal{top:1179px;font-size:6.3px;color:#444}
</style>
</head>
<body>

<!-- hero -->
<div class="abs hero" role="img" aria-label="Photo of an accountant's hands holding a pen over a tablet showing charts at a desk"></div>
<div class="abs hero-shade"></div>
<div class="abs brand"><span class="brand-mark"></span><span class="brand-name">KELVORAN FINANCIAL, LLC</span></div>
<nav class="abs nav">
  <a class="active" style="left:0">HOME</a>
  <a style="left:63px">ABOUT US</a>
  <a style="left:140px">SERVICES</a>
  <a style="left:214px">CONTACT US</a>
  <svg style="position:absolute;left:275px;top:0" width="9" height="9" viewBox="0 0 10 10"><circle cx="4" cy="4" r="3" fill="none" stroke="#fff" stroke-width="1.5"/><line x1="6.3" y1="6.3" x2="9" y2="9" stroke="#fff" stroke-width="1.5"/></svg>
</nav>
<div class="abs hero-mark"></div>
<div class="abs hero-title heading">KELVORAN FINANCIAL, LLC</div>
<div class="abs hero-rule"></div>
<div class="abs hero-tag heading">Accounting · Audit · Tax Services</div>
<div class="abs slide-arrow" style="left:23px"><svg width="16" height="16" viewBox="0 0 16 16"><path d="M9 5 6 8l3 3" fill="none" stroke="rgba(255,255,255,.7)"/></svg></div>
<div class="abs slide-arrow" style="left:652px"><svg width="16" height="16" viewBox="0 0 16 16"><path d="M7 5l3 3-3 3" fill="none" stroke="rgba(255,255,255,.7)"/></svg></div>

<!-- services -->
<section class="abs services">
  <div class="abs service" style="left:0">
    <div class="service-icon"><svg width="25" height="25" viewBox="0 0 25 25"><rect x="5" y="2" width="15" height="21" rx="1" fill="none" stroke="#fff" stroke-width="1.5"/><rect x="8" y="5" width="9" height="4" fill="#fff"/><g fill="#fff"><rect x="8" y="11" width="2.5" height="2.5"/><rect x="11.3" y="11" width="2.5" height="2.5"/><rect x="14.5" y="11" width="2.5" height="2.5"/><rect x="8" y="15" width="2.5" height="2.5"/><rect x="11.3" y="15" width="2.5" height="2.5"/><rect x="14.5" y="15" width="2.5" height="2.5"/><rect x="8" y="19" width="2.5" height="2"/><rect x="11.3" y="19" width="2.5" height="2"/><rect x="14.5" y="19" width="2.5" height="2"/></g></svg></div>
    <h3>OFFERING ACCOUNTING</h3>
    <p>Lorem ipsum dolor sit amet, consectetur adipisicing elit, sed do eiusmod tempor iunt ut labore et dolore magna aliqua. eiusmod</p>
    <svg class="btn-slant" viewBox="0 0 90 16"><polygon points="6,0 12,0 6,16 0,16" fill="#444"/><polygon points="20,0 90,0 82,16 12,16" fill="#0b2a78"/></svg>
    <span class="abs" style="left:84px;top:143px;font-size:6px;font-weight:600;color:#fff">READ MORE</span>
  </div>
  <div class="abs service" style="left:193px">
    <div class="service-icon"><svg width="25" height="25" viewBox="0 0 25 25"><rect x="4" y="3" width="13" height="18" fill="none" stroke="#fff" stroke-width="1.5"/><g stroke="#fff" stroke-width="1.2"><line x1="7" y1="8" x2="14" y2="8"/><line x1="7" y1="11" x2="14" y2="11"/><line x1="7" y1="14" x2="12" y2="14"/></g><line x1="20" y1="4" x2="20" y2="19" stroke="#fff" stroke-width="2.5"/></svg></div>
    <h3>AUDITING SERVICES</h3>
    <p>Lorem ipsum dolor sit amet, consectetur adipisicing elit, sed do eiusmod tempor iunt ut labore et dolore magna aliqua. eiusmod</p>
    <svg class="btn-slant" viewBox="0 0 90 16"><polygon points="6,0 12,0 6,16 0,16" fill="#444"/><polygon points="20,0 90,0 82,16 12,16" fill="#0b2a78"/></svg>
    <span class="abs" style="left:84px;top:143px;font-size:6px;font-weight:600;color:#fff">READ MORE</span>
  </div>
  <div class="abs service" style="left:386px">
    <div class="service-icon"><svg width="25" height="25" viewBox="0 0 25 25"><rect x="2" y="5" width="19" height="14" fill="none" stroke="#fff" stroke-width="1.5"/><rect x="5" y="8" width="9" height="5" fill="none" stroke="#fff"/><g stroke="#fff"><line x1="16" y1="9" x2="19" y2="9"/><line x1="16" y1="12" x2="19" y2="12"/><line x1="5" y1="16" x2="19" y2="16"/></g></svg></div>
    <h3>TAX PREPARATION</h3>
    <p>Lorem ipsum dolor sit amet, consectetur adipisicing elit, sed do eiusmod tempor iunt ut labore et dolore magna aliqua. eiusmod</p>
    <svg class="btn-slant" viewBox="0 0 90 16"><polygon points="6,0 12,0 6,16 0,16" fill="#444"/><polygon points="20,0 90,0 82,16 12,16" fill="#0b2a78"/></svg>
    <span class="abs" style="left:84px;top:143px;font-size:6px;font-weight:600;color:#fff">READ MORE</span>
  </div>
</section>
<svg class="abs services-tail" viewBox="0 0 578 18"><polygon points="0,0 578,0 578,4 289,18 0,4" fill="#f5f5f5"/></svg>

<!-- welcome -->
<section class="abs welcome">
  <div class="abs" style="left:0;top:0;width:691px;height:296px" role="img" aria-label="Night skyline of a city lit up under a deep blue sky"></div>
  <h2 class="heading">Welcome To Kelvoran Financial</h2>
  <div class="welcome-rule"></div><div class="welcome-dot"></div>
  <p>Lorem ipsum dolor sit amet, consectetur adipiscing elit, sed do eiusmod tempor incididunt ut labore et dolore magna aliqua. Ut enim ad minim veniam, quis nostrud exercitation ullamco laboris nisi ut aliquip ex ea commodo consequat. Duis aute irure dolor in reprehenderit in voluptate velit esse cillum dolore eu fugiat nulla pariatur. Excepteur sint occaecat cupidatat non proident, sunt in culpa qui officia deserunt mollit anim id est laborum Lorem ipsum dolor sit amet, consectetur adipiscing elit.</p>
  <svg class="ghost" viewBox="0 0 120 22"><polygon points="10,0 20,0 10,22 0,22" fill="#fff"/><polygon points="30,0.5 119,0.5 102,21.5 14,21.5" fill="none" stroke="#fff"/></svg>
  <span class="abs" style="left:325px;top:126px;font-size:6.5px;font-weight:600;color:#fff">READ MORE</span>
  <div class="abs person" style="left:64px">
    <div class="person-photo" role="img" aria-label="Portrait photo of a smiling team member"></div>
    <h4>JOHN DOE</h4>
    <p>Lorem ipsum dolor sit amet, consecte adipiscing elit, sed do eiusmod tempor incididunt ut labore et dolore magna aliqua.</p>
    <span class="outline">READ MORE</span>
  </div>
  <div class="abs person" style="left:355px">
    <div class="person-photo" role="img" aria-label="Portrait photo of a team member holding a notebook"></div>
    <h4>JOHN DOE</h4>
    <p>Lorem ipsum dolor sit amet, consecte adipiscing elit, sed do eiusmod tempor incididunt ut labore et dolore magna aliqua.</p>
    <span class="outline">READ MORE</span>
  </div>
</section>

<!-- newsletter -->
<section class="abs newsletter">
  <h2 class="heading">SIGNUP FOR NEWSLETTER</h2>
  <p>Lorem Ipsum is simply dummy text of the printing and typesetting industry. Lorem Ipsum has been the industry's standard dummy text ever since the 1500s, when an unknown printer took a galley of type and scrambled it to make a type specimen book.</p>
  <div class="field" style="left:119px;width:170px">Enter Your Name</div>
  <div class="field" style="left:293px;width:170px">Enter Your E-Mail Address</div>
  <div class="subscribe">SUBSCRIBE NOW !</div>
</section>

<!-- footer band -->
<svg class="abs band" viewBox="0 0 691 36"><polygon points="0,11 395,11 370,36 0,36" fill="#0b2a78"/><polygon points="412,0 691,0 691,36 380,36" fill="#4a4a4a"/><polygon points="395,11 400,11 375,36 370,36" fill="#fff"/></svg>

<!-- footer -->
<div class="abs footer-mark"></div>
<div class="abs badge" style="left:141px;width:53px;background:#f6f6f6"></div>
<div class="abs badge" style="left:199px;width:52px;background:#f6f6f6"></div>
<div class="abs badge" style="left:257px;width:74px;background:#0b2a78;border-color:#0b2a78"></div>
<div class="abs social" style="left:206px"></div>
<div class="abs social" style="left:225px"></div>
<div class="abs social" style="left:244px"></div>
<div class="abs social" style="left:264px"></div>
<nav class="abs links"><a>Home</a><a>About Us</a><a>Services</a><a>Contact Us</a></nav>
<div class="abs contact">
  <svg style="top:3px" width="7" height="9" viewBox="0 0 7 9"><path d="M3.5 0A3 3 0 0 0 .5 3c0 2.2 3 6 3 6s3-3.8 3-6a3 3 0 0 0-3-3z" fill="#0b2a78"/><circle cx="3.5" cy="3" r="1" fill="#fff"/></svg>
  <div style="top:0">641 Linden Row NE Suite 410 Marlow, GA 30512 555.014.2290</div>
  <svg style="top:37px" width="8" height="6" viewBox="0 0 8 6"><rect width="8" height="6" fill="#0b2a78"/><path d="M0 0l4 3 4-3" fill="none" stroke="#fff" stroke-width=".7"/></svg>
  <div style="top:34px">: hello@kelvoranfinancial.example</div>
  <svg style="top:55px" width="8" height="7" viewBox="0 0 8 7"><rect x=".5" y=".5" width="7" height="4.5" fill="none" stroke="#0b2a78"/><rect x="2" y="6" width="4" height="1" fill="#0b2a78"/></svg>
  <div style="top:51px">: www.kelvoranfinancial.example</div>
</div>
<div class="abs legal-rule"></div>
<div class="abs legal" style="left:61px">© 2015 Kelvoran Financial &nbsp;|&nbsp; All Rights Reserved</div>
<div class="abs legal" style="left:506px">Terms &amp; Conditions &nbsp;|&nbsp; Privacy Policy</div>

</body>
</html>
```